Brackenlow Rotors Business Card

We are a new company based in Central Queensland, Australia that uses specalised drones (Vantorq Sprayhawk K40) to undertake mainly agricultural operations, like spraying weeds, spraying crops, spreading seed etc. I have attached a Plimsy proof of a card I was thinking along the lines of - purely a start point. The drone used in the business card MUST be a Vantorq Sprayhawk K40.
I am very open to other ideas, especially fonts and layout. I don't have website etc set up yet.
The images are stock and easily interchangeable, I just ask that any background images reflect the local central Queensland area. The photo of the drone is not even complete (propellers cut off) and I need a new stock photo – I’m not sure if this is an issue, or I can pay for an image if need be. PLEASE FIND AN SPRAYHAWK K40 image - 4 sprayers, not 6.
The logo/business name is very draft and looking for further ideas, ideally incorporating drones or agriculture design elements into the design of the business name. The business name needs work on the graphic/design – it is a draft that I have included, the drone propellers (being a different colour) are DRAFT only and intended for changes. PLEASE DO NOT USE THE DRONE PORPELLER I HAVE USED AS A DRAFT. TRY TO FIND SOMETHING ELSE.. The arrow is a shape and not aligned in any way, I would also like ideas on different fonts and additional elements, like air streams, aviation elements, aviation or country western (farming like) themes and fonts etc.
Ideally looking at staying within the blue, green and yellow colours, keeping with an natural, outdoorsy, environmental feel.

Target Market(s)

Farmers, Agriculture, Local Governments, Land Managers

Industry/Entity Type

Agriculture, Drones, Aviation

Contact Information for Business Card

Agricultural Drone (Vantorq Sprayhawk K40), Farming, Business Name.

Font styles to use
Sans Serif

Colors
0054AA
0677BA
7BADD7
CADEEF
E8F1F8
0094D4
00A9DD
6FCCEA
C7EBF8
E9F6FB
00AB8E
00BBA5
67D7C9
C6EFE9
E9F9F6
59FF00
82FF00
B8FF75
E3FFCB
F4FFEA

Requirements
Must have
• Vantorq Sprayhawk K40 Drone
Should not have
• Tractors

```html
<!DOCTYPE html>
<html lang="en">
<head>
<meta charset="utf-8">
<title>Brackenlow Rotors Business Card</title>
<link rel="stylesheet" href="https://fonts.googleapis.com/css2?family=Montserrat:ital,wght@0,600;0,700;0,800;1,800&family=Cinzel:wght@600&display=swap">
<style>
  :root {
    --olive: #7f8c3a;
    --slate: #4a5670;
    --paper: #ffffff;
    --backdrop: #eeeeee;
    --drone-light: #e4e6e8;
    --drone-dark: #9aa0a6;
  }
  * { margin: 0; padding: 0; box-sizing: border-box; }
  html, body {
    width: 1200px;
    height: 1199px;
    overflow: hidden;
    background: var(--backdrop);
    font-family: "Montserrat", Arial, sans-serif;
  }
  .card {
    position: absolute;
    left: 257px;
    width: 686px;
    height: 392px;
    overflow: hidden;
  }
  .card-front {
    top: 190px;
    background: var(--olive);
    color: var(--paper);
    text-align: center;
  }
  .brand-name {
    position: absolute;
    left: 0;
    right: 0;
    top: 126px;
    font-weight: 800;
    font-size: 42px;
    line-height: 48px;
    letter-spacing: 1px;
    text-transform: uppercase;
  }
  .brand-tagline {
    position: absolute;
    left: 0;
    right: 0;
    top: 228px;
    font-family: "Cinzel", Georgia, serif;
    font-weight: 600;
    font-size: 16px;
    letter-spacing: 1.5px;
  }
  .card-back {
    top: 625px;
    background: var(--paper);
    color: var(--slate);
  }
  .card-wave {
    position: absolute;
    left: 0;
    top: 0;
    width: 686px;
    height: 392px;
  }
  .person-name {
    position: absolute;
    left: 43px;
    top: 44px;
    font-weight: 800;
    font-style: italic;
    font-size: 30px;
    color: var(--olive);
    text-transform: uppercase;
  }
  .person-title {
    position: absolute;
    left: 45px;
    top: 83px;
    font-weight: 700;
    font-size: 18px;
    text-transform: uppercase;
  }
  .contact-list {
    position: absolute;
    left: 43px;
    top: 174px;
    list-style: none;
  }
  .contact-item {
    display: flex;
    align-items: flex-start;
    font-weight: 700;
    font-size: 18px;
    line-height: 23px;
    margin-bottom: 4px;
    text-transform: uppercase;
  }
  .contact-icon {
    width: 18px;
    height: 18px;
    margin: 2px 9px 0 0;
    flex: none;
    fill: var(--olive);
  }
  .contact-item.address .contact-icon { margin-top: 25px; }
  .drone-photo {
    position: absolute;
    left: 345px;
    top: 110px;
    width: 300px;
    height: 108px;
    border-radius: 6px;
    background: radial-gradient(ellipse at center, var(--drone-dark) 0%, var(--drone-light) 60%, var(--paper) 100%);
  }
</style>
</head>
<body>
  <section class="card card-front">
    <h1 class="brand-name">Brackenlow<br>Rotors</h1>
    <p class="brand-tagline">Servicing Central Queensland</p>
  </section>

  <section class="card card-back">
    <svg class="card-wave" viewBox="0 0 686 392" aria-hidden="true">
      <path d="M0,328 C110,358 240,385 380,362 C500,342 600,304 686,306 L686,392 L0,392 Z" fill="var(--olive)"/>
    </svg>
    <div class="drone-photo" role="img" aria-label="Photo of a Vantorq Sprayhawk K40 agricultural spraying drone in flight"></div>
    <h2 class="person-name">Tom Harlow</h2>
    <p class="person-title">CEO &amp; Founder</p>
    <ul class="contact-list">
      <li class="contact-item">
        <svg class="contact-icon" viewBox="0 0 24 24"><path d="M6.6 10.8a15.1 15.1 0 0 0 6.6 6.6l2.2-2.2a1 1 0 0 1 1-.25 11.4 11.4 0 0 0 3.6.57 1 1 0 0 1 1 1V20a1 1 0 0 1-1 1A17 17 0 0 1 3 4a1 1 0 0 1 1-1h3.5a1 1 0 0 1 1 1c0 1.25.2 2.450.57 3.6a1 1 0 0 1-.25 1z"/></svg>
        <span>+1 (555) 204-7713</span>
      </li>
      <li class="contact-item">
        <svg class="contact-icon" viewBox="0 0 24 24"><path d="M12 2a10 10 0 1 0 0 20 10 10 0 0 0 0-20zm6.9 6h-2.9a15.7 15.7 0 0 0-1.4-3.6A8 8 0 0 1 18.9 8zM12 4c.8 1.2 1.5 2.5 1.9 4h-3.8c.4-1.5 1.1-2.8 1.9-4zM4.3 14a8 8 0 0 1 0-4h3.4a16.5 16.5 0 0 0 0 4zm.8 2h2.9c.3 1.3.8 2.5 1.4 3.6A8 8 0 0 1 5.1 16zM8 8H5.1a8 8 0 0 1 4.3-3.6C8.8 5.5 8.3 6.7 8 8zm4 12c-.8-1.2-1.5-2.5-1.9-4h3.8c-.4 1.5-1.1 2.8-1.9 4zm2.3-6H9.7a14.7 14.7 0 0 1 0-4h4.6a14.7 14.7 0 0 1 0 4zm.3 5.6c.6-1.1 1.1-2.3 1.4-3.6h2.9a8 8 0 0 1-4.3 3.6zm1.7-5.6a16.5 16.5 0 0 0 0-4h3.4a8 8 0 0 1 0 4z"/></svg>
        <span>Brackenlowrotors.com</span>
      </li>
      <li class="contact-item">
        <svg class="contact-icon" viewBox="0 0 24 24"><path d="M2 5h20v14H2zm2 2v.5l8 5 8-5V7zm0 2.9V17h16V9.9l-8 5z"/></svg>
        <span>Tom.harlow@brackenlow.com</span>
      </li>
      <li class="contact-item address">
        <svg class="contact-icon" viewBox="0 0 24 24"><path d="M12 2a7 7 0 0 0-7 7c0 5.2 7 13 7 13s7-7.8 7-13a7 7 0 0 0-7-7zm0 9.5A2.5 2.5 0 1 1 12 6.5a2.5 2.5 0 0 1 0 5z"/></svg>
        <span>118 Kelland Street,<br>Suite 4, Perryvale,<br>QLD 4702</span>
      </li>
    </ul>
  </section>
</body>
</html>
```